New word press website site design

We provide email marketing to aircraft brokers and dealers to assist in finding buyers for their aircraft.

Our target market to purchase our broadcasts are the aircraft sellers – NOT the buyers.

Our target market when sending the email broadcast, are the buyers (end users).

The website should target brokers and our email database targets the buyers.

We do not buy or sell aircraft as a company. We provide email marketing solutions to connect buyers and sellers of aircraft.

Our other site is vesseltrove.net and will be redesigned soon. Please use it as a reference as far as general scope but they layout can be completely different and should include helicopters only as far as imagery. The colors should be similar as the logos are similar, however we do NOT want both sites to be identical in use of primary color

Plenty of images and sample broadcasts attached to use as needed throughout the site.

Headlines listed below with some text copy.

In the event that we need to add more text, please use standard greek text as a place holder for the purposes of the mockup design.

Need to have a “SUBSCRIBE” button to join our mailing list.

Possible Headlines:

Exclusively Showcasing Rotor Wing Aircraft to the Global Marketplace

Showcasing Pre-Owned Helicopters Available For Sale, Lease, Trade, or Wanted for Acquisition.

Mobile-optimized Email Campaigns that Render Correctly Across all Devices

Targeted worldwide recipients that currently own, operate, or have an interest in rotor wing aircraft

STRONGEST Rotor Wing Database in the Industry

Text/Copy:

HOME
Rotorline Parade is one of most powerful marketing tools in the industry to utilize in reaching targeted buyers of pre-owned helicopters. Rotorline Parade provides the rotor wing aircraft market with a fast, effective, and affordable email broadcast solution to utilize in the marketing of Helicopters for sale.

Developed Exclusively to Parade Rotor Wing Aircraft to the Global marketplace, Rotorline Parade is a powerful tool designed to maximize leads and accelerate the sales process by providing the ability to reach a global network of Helicopter buyers in a matter of seconds.

DATABASE:

While Rotorline Parade is delivered to all known broker/dealers, our primary focus is in reaching end users. Our opt-in/opt-out recipient database is updated daily and developed specifically to deliver the latest details on helicopters available for sale or lease to the inboxes of a global network of Helicopter buyers and sellers.

· Helicopter Owners

· Helicopter Operators

· Helicopter Charter Services

· Helicopter Management Companies

· Corporate/Municipal Flight Departments

· Helicopter Pilots

· Senior Aviation Executives

· Wealth Management Firms

· High Net Worth Individuals

· Helicopter Broker/Dealers

Helicopter Tour/Travel Firms

· Off Shore Oil & Gas Production Firms

· Municipalities/Media/Medevac Firms

Our recipient database is continuously updated and developed specifically to reach buyers and sellers of Helicopters. This ensures that your Helicopter will be showcased to the right people. Rotorline Parade does not broadcast non-rotor wing aircraft and focuses exclusively on the Global Helicopter Market.

Broadcast Design:

Rotorline Parade broadcast ads are custom designed for you by incorporating your corporate image and branding. Because you have worked hard in developing your corporate image, we strive to maintain it while designing an ad that will showcase your Helicopter to its best advantage. Rotorline Parade utilizes Mobile-optimized Email Campaigns with Responsive Coding to render correctly across all devices

Once you have approved the design, we schedule the broadcast to be sent on the available date and time you request. The broadcast will link to your website and the results can be immediate. All email leads and replies will go to the email address that you provided.

Pricing:
Create a place holder for 3 Different Broadcast Packages

-Broadcast Package A
-Broadcast Package B
-Broadcast Package C

Target Market(s)

The target market is any person or company that has aircraft for sale. We work with brokers, dealers, and owners to assist in finding buyers for their aircraft using email marketing campaigns (Parade broadcasts).

Industry/Entity Type

Aviation

Colors
0255a3
00a990

Requirements
Nice to have
• Samples of helicopter for sale broadcast ads in /image gallery/slider

```html
<!DOCTYPE html>
<html lang="en">
<head>
<meta charset="utf-8">
<title>Skyreach Media Inc — Rotorline Parade</title>
<link href="https://fonts.googleapis.com/css2?family=Montserrat:wght@300;400;500;600&family=Poppins:wght@300;400;500;600&display=swap" rel="stylesheet">
<style>
  :root{
    --black:#000000;
    --ink:#111111;
    --red:#d0161b;
    --white:#ffffff;
    --grey-text:#7a7a7a;
    --footer:#1c1c1c;
    --line:#9a9a9a;
    --s1:#3b5998;
    --s2:#3fa8e0;
    --s3:#0e76a8;
    --s4:#c4302b;
    --s5:#2a5d84;
    --s6:#c8232c;
  }
  *{margin:0;padding:0;box-sizing:border-box}
  html,body{width:1200px;height:3333px;overflow:hidden;background:var(--white)}
  body{font-family:"Poppins",sans-serif;position:relative}
  .canvas{position:relative;width:1200px;height:3333px;overflow:hidden}

  /* hero */
  .hero{position:absolute;left:0;top:0;width:1200px;height:964px;background:var(--black)}
  .brand{position:absolute;top:50px;left:0;width:1200px;display:flex;justify-content:center;align-items:center;gap:20px}
  .brand-mark{width:30px;height:30px;background:var(--red)}
  .brand-name{font-family:"Montserrat",sans-serif;font-weight:600;color:var(--white);font-size:46px;letter-spacing:6px;line-height:1.15;text-align:center}
  .brand-name span{display:block;font-size:24px;letter-spacing:14px}
  .hero-rule{position:absolute;left:142px;width:916px;height:2px;background:var(--line)}
  .hero-title{position:absolute;top:254px;left:0;width:1200px;text-align:center;font-family:"Montserrat",sans-serif;font-weight:400;font-size:38px;line-height:57px;color:var(--white);letter-spacing:1px}
  .hero-photo{position:absolute;left:0;top:470px;width:1200px;height:440px;background:radial-gradient(ellipse 45% 38% at 52% 52%,#8a8d92 0%,#3a3c40 45%,#0b0b0c 80%,#000 100%)}

  /* welcome */
  .welcome{position:absolute;left:0;top:964px;width:1200px;height:514px;background:var(--white);text-align:center}
  .eyebrow{position:absolute;top:72px;width:100%;font-weight:500;font-size:30px;letter-spacing:5px;color:var(--ink)}
  .section-title{font-family:"Montserrat",sans-serif;font-weight:400;font-size:54px;letter-spacing:6px;color:var(--red)}
  .welcome .section-title{position:absolute;top:116px;width:100%}
  .welcome-copy{position:absolute;top:198px;left:100px;width:1000px;font-weight:300;font-size:23px;line-height:35px;color:var(--grey-text)}
  .btn-read{position:absolute;top:378px;left:506px;width:190px;height:52px;background:var(--ink);color:var(--white);font-weight:500;font-size:23px;line-height:52px;border-radius:3px}

  /* database */
  .database{position:absolute;left:0;top:1478px;width:1200px;height:760px;background:var(--black);color:var(--white)}
  .database .section-title{position:absolute;top:64px;width:100%;text-align:center}
  .database-copy{position:absolute;top:146px;left:80px;width:1040px;text-align:center;font-weight:300;font-size:23px;line-height:35.5px}
  .audience{position:absolute;top:342px;list-style:none;font-family:"Montserrat",sans-serif;font-weight:500;font-size:24px}
  .audience li{position:relative;height:51px;line-height:36px;padding-left:35px;white-space:nowrap}
  .audience li::before{content:"";position:absolute;left:0;top:12px;border-left:9px solid var(--white);border-top:6px solid transparent;border-bottom:6px solid transparent}
  .audience-left{left:67px}
  .audience-right{left:654px}
  .audience .small{font-size:21px}

  /* pricing */
  .pricing{position:absolute;left:0;top:2238px;width:1200px;height:929px;background:var(--white)}
  .pricing .section-title{position:absolute;top:72px;width:100%;text-align:center}
  .plan{position:absolute;top:162px;width:348px;height:551px;background:var(--white);box-shadow:0 2px 14px rgba(0,0,0,.22);text-align:center}
  .plan-photo{position:absolute;top:5px;left:5px;width:338px;height:231px}
  .plan-title{position:absolute;top:268px;width:100%;font-family:"Montserrat",sans-serif;font-weight:500;font-size:27px;color:var(--ink)}
  .plan-price{position:absolute;top:316px;width:100%;font-family:"Montserrat",sans-serif;font-weight:500;font-size:40px;color:var(--red)}
  .plan-copy{position:absolute;top:392px;left:0;width:100%;font-family:"Montserrat",sans-serif;font-weight:400;font-size:20.5px;line-height:34px;color:var(--ink);white-space:nowrap}
  .plan-a{left:44px}.plan-b{left:426px}.plan-c{left:807px}
  .photo-a{background:linear-gradient(160deg,#1a1a1c 0%,#4a4a4e 50%,#151516 100%)}
  .photo-b{background:radial-gradient(ellipse 60% 55% at 50% 55%,#5a5c60 0%,#262628 60%,#0e0e0f 100%)}
  .photo-c{background:linear-gradient(180deg,#6f8fb8 0%,#a9bdd3 55%,#3b4350 100%)}
  .btn-subscribe{position:absolute;top:797px;left:504px;width:214px;height:52px;background:var(--red);color:var(--white);font-family:"Montserrat",sans-serif;font-weight:600;font-size:24px;letter-spacing:3px;line-height:52px;text-align:center;border-radius:3px}

  /* footer */
  .footer{position:absolute;left:0;top:3167px;width:1200px;height:166px;background:var(--footer)}
  .social{position:absolute;top:57px;left:362px;display:flex;gap:7px;list-style:none}
  .social li{width:70px;height:54px}
  .footer-code{position:absolute;top:68px;right:32px;color:#cfcfcf;font-size:21px}
</style>
</head>
<body>
<div class="canvas">

  <header class="hero">
    <div class="brand">
      <span class="brand-mark"></span>
      <div class="brand-name">SKYREACH<span>MEDIA INC</span></div>
    </div>
    <div class="hero-rule" style="top:222px"></div>
    <h1 class="hero-title">EXCLUSIVELY SHOWCASING ROTOR WING AIRCRAFT<br>TO THE GLOBAL MARKETPLACE</h1>
    <div class="hero-rule" style="top:402px"></div>
    <div class="hero-photo" role="img" aria-label="Silver and black helicopter parked on a dark studio floor"></div>
  </header>

  <section class="welcome">
    <p class="eyebrow">WELCOME TO</p>
    <h2 class="section-title">SKYREACH MEDIA</h2>
    <p class="welcome-copy">Rotorline Parade is one of most powerful marketing tools in the industry to utilize in reaching targeted buyers of pre-owned helicopters. Rotorline Parade provides the rotor wing aircraft market with a fast, effective, and affordable email broadcast solution to utilize in the marketing of Helicopters for sale.</p>
    <a class="btn-read">Read More &gt;</a>
  </section>

  <section class="database">
    <h2 class="section-title">DATABASE</h2>
    <p class="database-copy">While Rotorline Parade is delivered to all known broker/dealers, our primary focus is in reaching end users. Our opt-in/opt-out recipient database is updated daily and developed specifically to deliver the latest details on helicopters available for sale or lease to the inboxes of a global network of Helicopter buyers and sellers.</p>
    <ul class="audience audience-left">
      <li>Helicopter Owners</li>
      <li>Helicopter Operators</li>
      <li>Helicopter Charter Services</li>
      <li>Helicopter Management Companies</li>
      <li>Corporate/Municipal Flight Departments</li>
      <li>Helicopter Pilots</li>
      <li>Senior Aviation Executives</li>
    </ul>
    <ul class="audience audience-right">
      <li>Wealth Management Firms</li>
      <li>High Net Worth Individuals</li>
      <li>Helicopter Broker/Dealers</li>
      <li>Helicopter Management Companies</li>
      <li class="small">Helicopter Tour/Travel Firms</li>
      <li>Off Shore Oil &amp; Gas Production Firms</li>
      <li>Municipalities/Media/Medevac Firms</li>
    </ul>
  </section>

  <section class="pricing">
    <h2 class="section-title">PRICING</h2>
    <article class="plan plan-a">
      <div class="plan-photo photo-a" role="img" aria-label="Dark executive helicopter with red accent lighting"></div>
      <h3 class="plan-title">TITLE GOES HERE</h3>
      <p class="plan-price">$ 265.00</p>
      <p class="plan-copy">Lorem Ipsum is simply<br>dummy text of the printing<br>and typesetting industry.<br>Lorem Ipsum has been</p>
    </article>
    <article class="plan plan-b">
      <div class="plan-photo photo-b" role="img" aria-label="Helicopter lit in a dark hangar"></div>
      <h3 class="plan-title">TITLE GOES HERE</h3>
      <p class="plan-price">$ 365.00</p>
      <p class="plan-copy">Lorem Ipsum is simply<br>dummy text of the printing<br>and typesetting industry.<br>Lorem Ipsum has been</p>
    </article>
    <article class="plan plan-c">
      <div class="plan-photo photo-c" role="img" aria-label="Helicopter on a rooftop pad with a city skyline behind"></div>
      <h3 class="plan-title">TITLE GOES HERE</h3>
      <p class="plan-price">$ 465.00</p>
      <p class="plan-copy">Lorem Ipsum is simply<br>dummy text of the printing<br>and typesetting industry.<br>Lorem Ipsum has been</p>
    </article>
    <a class="btn-subscribe">SUBSCRIBE</a>
  </section>

  <footer class="footer">
    <ul class="social">
      <li style="background:var(--s1)"></li>
      <li style="background:var(--s2)"></li>
      <li style="background:var(--s3)"></li>
      <li style="background:var(--s4)"></li>
      <li style="background:var(--s5)"></li>
      <li style="background:var(--s6)"></li>
    </ul>
    <span class="footer-code">C24</span>
  </footer>

</div>
</body>
</html>
```